Website Online Research Solutions

We are a small European high-tech online research company.
With our own state of the art software we run online panels and are conducting reseach for companies. Partly research via our own panel and partly via panels we maintain for our customers.
Our current website is old and outdatet: www.pravelo.nl.
We are in the process to change the content of the site. We want a modern, european and businesslike design for our new website.
Our logo has to stay the same (left uppersite of our website and attached) but can be changed a little to adapt it to the new design of the website. The colors of the site are up to you.
Target Market(s)
Marketeers and researchers of large and middle size companies in all kind of fields.
Industry/Entity Type
Online
Look and feel
Each slider illustrates characteristics of the customer's brand and the style your logo design should communicate.

```html
<!DOCTYPE html>
<html lang="nl">
<head>
<meta charset="utf-8">
<title>Pravelo – Online Research Solutions</title>
<link href="https://fonts.googleapis.com/css2?family=PT+Sans+Narrow:wght@400;700&display=swap" rel="stylesheet">
<style>
  :root {
    --brown: #8a6c4e;
    --gold: #c6a04c;
    --gold-dark: #b48f3e;
    --text: #6e6a66;
    --tab-border: #d6cfc6;
    --page-top: #fbfbfd;
    --page-bottom: #e6e7ea;
    --line: #b89a7a;
  }
  * { box-sizing: border-box; margin: 0; padding: 0; }
  html, body { width: 1200px; height: 900px; overflow: hidden; }
  body {
    position: relative;
    font-family: "PT Sans Narrow", "Arial Narrow", sans-serif;
    background: linear-gradient(180deg, var(--page-top) 0%, var(--page-top) 70%, var(--page-bottom) 100%);
    color: var(--text);
  }
  .brand {
    position: absolute; left: 64px; top: 18px;
    display: flex; align-items: center; gap: 26px;
  }
  .brand-mark {
    width: 128px; height: 128px; border-radius: 50%;
    background: var(--gold-dark);
  }
  .brand-name {
    font-size: 30px; line-height: 32px; color: var(--brown); font-weight: 400;
  }
  .search {
    position: absolute; left: 911px; top: 55px; width: 248px; height: 26px;
    display: flex; border-radius: 13px; overflow: hidden;
    border: 1px solid #d8d2c8; background: #fff;
    box-shadow: 0 2px 3px rgba(0,0,0,.15);
  }
  .search input { flex: 1; border: 0; outline: 0; padding: 0 12px; background: transparent; }
  .search button {
    width: 52px; border: 0; background: var(--brown); color: #fff;
    font-family: inherit; font-size: 13px; text-transform: uppercase;
  }
  .main-nav {
    position: absolute; left: 374px; top: 123px; display: flex;
  }
  .main-nav a {
    width: 112px; height: 37px; display: flex; align-items: center; justify-content: center;
    border: 1px solid var(--tab-border); border-bottom: 0; border-radius: 8px 8px 0 0;
    background: linear-gradient(#ffffff, #f1f0ee);
    color: var(--brown); font-size: 17px; text-decoration: none;
  }
  .main-nav a.active { background: linear-gradient(#d4b15e, var(--gold-dark)); color: #fff; border-color: var(--gold-dark); }
  .rule { position: absolute; left: 36px; width: 1128px; height: 4px; background: var(--line); }
  .rule.top { top: 160px; }
  .rule.bottom { top: 442px; height: 3px; }
  .hero {
    position: absolute; left: 36px; top: 164px; width: 1128px; height: 278px;
    background: linear-gradient(90deg, #c9d3e1 0%, #e3e8f0 35%, #2c3e66 55%, #3a4f7a 75%, #dfe5ee 100%);
  }
  .intro {
    position: absolute; left: 64px; top: 478px; width: 660px;
  }
  .intro h1 { font-weight: 400; font-size: 28px; line-height: 31px; color: var(--brown); }
  .intro h1 span { display: block; padding-left: 83px; color: var(--gold); white-space: nowrap; }
  .intro p { margin-top: 26px; font-size: 16px; line-height: 25px; white-space: nowrap; }
  .sites-title { margin-top: 14px; font-weight: 700; font-size: 16px; color: var(--brown); }
  .sites { list-style: none; margin-top: 6px; }
  .sites li { position: relative; padding-left: 20px; font-size: 15px; line-height: 25px; }
  .sites li::before {
    content: ""; position: absolute; left: 0; top: 8px;
    border-left: 8px solid var(--brown); border-top: 5px solid transparent; border-bottom: 5px solid transparent;
  }
  .network-art {
    position: absolute; left: 712px; top: 482px; width: 447px; height: 353px;
    background: radial-gradient(ellipse at 50% 70%, #c6dcef 0%, #e4edf5 45%, rgba(240,242,246,0) 75%);
  }
</style>
</head>
<body>
  <header>
    <div class="brand">
      <div class="brand-mark"></div>
      <div class="brand-name">Pravelo<br>Online Research Solutions</div>
    </div>
    <form class="search">
      <input type="text" aria-label="Zoeken">
      <button type="button">Search</button>
    </form>
    <nav class="main-nav">
      <a class="active" href="#">Algemeen</a>
      <a href="#">Producten</a>
      <a href="#">Demo's</a>
      <a href="#">Media</a>
      <a href="#">Referenties</a>
      <a href="#">Personeel</a>
      <a href="#">Contact</a>
    </nav>
  </header>
  <div class="rule top"></div>
  <div class="hero" role="img" aria-label="Foto van drie zakenmensen in pak die samen grafieken en onderzoeksresultaten bekijken"></div>
  <div class="rule bottom"></div>
  <main class="intro">
    <h1>Pravelo is gespecialiseerd in online gegevensverzameling en <span>analyse en is werkzaam voor internationale opdrachtgevers.</span></h1>
    <p>Het bedrijf werd opgericht in 1996 en is gevestigd in Marendam, een kleine havenplaats<br>
    boven Amsterdam. Onze produkten zijn ontwikkeld op basis van Vecta, een krachtige en uitermate<br>
    flexibele onderzoekstool voor het verzamelen &amp; verwerken van (online) researchgegevens.<br>
    Vecta werd ontwikkeld dóór opinieonderzoekers vóór opinieonderzoekers.<br>
    Ons team bestaat uit zowel opinieonderzoekers als programmeurs met vele jaren ervaring op<br>
    het gebied van opinieonderzoek en met name met online toepassingen daarvoor.</p>
    <h2 class="sites-title">Deze bekende sites zijn ontwikkeld en worden beheerd door Pravelo BV:</h2>
    <ul class="sites">
      <li>www.meetpunt.nl</li>
      <li>www.spiegelzaal.nl</li>
      <li>www.jongmeter.nl</li>
      <li>KW klantenpanel</li>
    </ul>
  </main>
  <div class="network-art" role="img" aria-label="Illustratie van een gestippelde wereldkaart met een server die via pijlen verbonden is met computers"></div>
</body>
</html>
```